Brevin Electric Ltd

Looking for a single page website and Facebook page design. I am an electrical contractor based on Vancouver Island. I do service, custom homes, residential and commercial installations. My company just started out, so I don't have any pictures of installs yet. I have 25 years experience. I would like the colors to be my logo colors black and I have a black Torvik Ridgeman that will be my vehicle which I will have a wrap for.
Updates

I just posted the contest today, not sure why the deadline is the same day.

Went on vacation/holiday

Industry/Entity Type

Electrician

Requirements
Must have
• Services provided, About me section, quote section,
Nice to have
• I am not quite sure yet, I need to see some designs first .

```html
<!DOCTYPE html>
<html lang="en">
<head>
<meta charset="utf-8">
<title>Brevin Electric Ltd</title>
<link rel="stylesheet" href="https://fonts.googleapis.com/css2?family=Montserrat:wght@400;500;600;700&family=Arimo:wght@400;700&display=swap">
<style>
:root{
  --gold:#f2b705;
  --gold-deep:#e6aa00;
  --black:#111111;
  --ink:#222222;
  --grey:#555555;
  --pale:#ececec;
  --white:#ffffff;
  --head:'Montserrat',sans-serif;
  --body:'Arimo',sans-serif;
}
*{box-sizing:border-box;margin:0;padding:0}
html,body{width:1200px;height:4221px;overflow:hidden;background:var(--white);font-family:var(--body);color:var(--ink)}
.page{position:relative;width:1200px;height:4221px}
.abs{position:absolute}
.fill{position:absolute}

/* header */
.topbar{left:0;top:0;width:1200px;height:56px;background:var(--gold)}
.topbar .info{position:absolute;right:190px;top:21px;font:500 14px var(--head);color:var(--white);display:flex;gap:26px}
.brand-block{left:0;top:0;width:360px;height:128px;background:var(--black);clip-path:polygon(0 0,100% 0,318px 100%,0 100%)}
.brand{left:110px;top:16px;display:flex;flex-direction:column;align-items:center;gap:8px}
.brand .mark{width:64px;height:64px;border:4px solid var(--gold);border-radius:50%}
.brand .name{font:600 15px var(--head);color:var(--white);letter-spacing:.3px}
.nav{left:472px;top:86px;display:flex;gap:44px;font:500 14px var(--head);color:var(--ink)}
.nav .on{color:var(--gold)}
.nav-search{left:1072px;top:87px;width:12px;height:12px;border:2px solid var(--gold);border-radius:50%}

/* hero */
.hero{left:0;top:128px;width:1200px;height:713px;background:linear-gradient(100deg,#6d6a5a 0%,#8b8a80 35%,#b9b2a0 60%,#7a6f55 100%)}
.hero h1{position:absolute;left:108px;top:168px;font:600 80px/88px var(--head);color:var(--white);letter-spacing:3px}
.hero p{position:absolute;left:112px;top:360px;width:440px;font:400 17px/32px var(--head);color:var(--white)}
.btn{display:flex;align-items:center;justify-content:center;background:var(--gold);color:var(--white);font:600 16px var(--head);border-radius:30px}
.hero .btn{position:absolute;left:112px;top:488px;width:170px;height:58px;font-size:18px}
.dots{position:absolute;left:577px;top:688px;display:flex;gap:8px}
.dots span{width:10px;height:10px;border-radius:50%;background:var(--white)}
.dots .on{background:var(--gold)}

/* section titles */
.title{left:0;width:1200px;text-align:center;font:600 34px var(--head);color:var(--black)}
.title b{color:var(--gold);font-weight:600}
.rule{width:42px;height:3px;background:var(--gold)}
.sub{left:0;width:1200px;text-align:center;font:400 15px var(--body);color:var(--grey)}

/* service cards */
.card{top:1011px;width:309px;height:467px;background:var(--black);text-align:center;color:var(--white)}
.card.gold{background:var(--gold)}
.card .photo{height:243px}
.card h3{margin-top:36px;font:600 21px var(--head)}
.card p{margin:16px auto 0;width:260px;font:400 13px/26px var(--body)}
.card .more{margin:18px auto 0;width:124px;height:42px;display:flex;align-items:center;justify-content:center;border:1.5px solid var(--white);border-radius:22px;font:600 14px var(--head)}

/* about */
.frame{left:72px;top:1582px;width:336px;height:298px;border:12px solid #d7d7d7;border-right:none;border-bottom:none}
.pattern-area{left:70px;top:2000px;width:210px;height:215px;background:var(--pale)}
.about-photo{left:113px;top:1623px;width:452px;height:531px;background:linear-gradient(160deg,#6b6f73,#a9acae 55%,#d9d6cf)}
.badge{left:380px;top:2000px;width:238px;height:213px;background:var(--gold);border:4px solid var(--black);text-align:center;color:var(--white)}
.badge .num{font:600 104px/1 var(--head);margin-top:30px}
.badge .lbl{font:500 16px var(--head);margin-top:8px}
.about-text{left:680px;top:1668px;width:400px}
.about-text .hi{font:500 25px var(--head);color:var(--black)}
.about-text h2{font:600 32px var(--head);color:var(--gold);margin-top:12px}
.about-text .line{width:394px;height:1px;background:var(--gold);margin-top:14px;position:relative}
.about-text .line:before{content:"";position:absolute;left:0;top:-1px;width:48px;height:3px;background:var(--gold)}
.about-text p{margin-top:36px;font:400 13.5px/26px var(--body);color:var(--grey);text-align:justify}
.about-text .btn{margin-top:26px;width:150px;height:50px}

/* featured */
.featured{left:0;top:2296px;width:1200px;height:546px;background:linear-gradient(90deg,#1c2233 0%,#2e3040 38%,#6b4a2e 60%,#a77c3c 80%,#50463e 100%)}
.featured h2{position:absolute;left:108px;top:100px;font:600 42px var(--head);color:var(--white)}
.featured .rule{position:absolute;left:110px;top:162px;width:60px}
.featured p{position:absolute;left:111px;top:186px;width:382px;font:400 13.5px/25.5px var(--body);color:var(--white);text-align:justify}
.featured .btn{position:absolute;left:111px;top:386px;width:150px;height:52px}

/* blog */
.post{top:3000px;width:476px;height:445px;background:var(--white);box-shadow:0 0 6px rgba(0,0,0,.14)}
.post .photo{height:272px;position:relative}
.post .date{position:absolute;right:20px;top:22px;width:80px;height:80px;border-radius:50%;background:var(--gold);color:var(--white);text-align:center;font:600 26px/1 var(--head);padding-top:16px}
.post .date small{display:block;font:500 14px var(--head);margin-top:2px}
.post h3{margin:36px 30px 0;font:600 20px var(--head);color:var(--black)}
.post p{margin:16px 30px 0;font:400 13px/22px var(--body);color:var(--grey)}

/* contact */
.contact{left:0;top:3516px;width:1200px;height:475px;background:linear-gradient(90deg,var(--gold-deep),var(--gold) 60%,#f5c42a)}
.cbrand{position:absolute;left:112px;top:40px;display:flex;flex-direction:column;align-items:center;gap:14px}
.cbrand .mark{width:124px;height:124px;border:5px solid var(--white);border-radius:50%}
.cbrand .name{font:600 20px var(--head);color:var(--white)}
.crow{position:absolute;left:112px;display:flex;gap:16px;align-items:center;color:var(--white)}
.crow .ic{width:44px;height:44px;border:2px solid var(--white);border-radius:50%;display:flex;align-items:center;justify-content:center}
.crow b{display:block;font:500 17px var(--head);line-height:20px}
.crow span{font:400 13px var(--head)}
.contact h2{position:absolute;left:556px;top:40px;font:500 30px var(--head);color:var(--white)}
.contact .rule{position:absolute;left:558px;top:86px;background:var(--white)}
.field{position:absolute;border:1.5px solid rgba(255,255,255,.75);border-radius:4px;font:500 12px var(--head);color:var(--white);padding:14px 16px}
.submit{position:absolute;left:557px;top:404px;width:133px;height:48px;display:flex;align-items:center;justify-content:center;background:var(--black);color:var(--white);font:600 15px var(--head);border-radius:3px}

/* footer */
.footer{left:0;top:3991px;width:1200px;height:230px;background:var(--black);color:var(--white)}
.fnav{position:absolute;left:0;width:1200px;top:56px;display:flex;justify-content:center;gap:44px;font:500 14px var(--head)}
.fsoc{position:absolute;left:495px;top:110px;display:flex;gap:7px}
.fsoc span{width:36px;height:36px;border:1.5px solid var(--white);border-radius:50%;display:flex;align-items:center;justify-content:center}
.copy{position:absolute;left:0;width:1200px;top:176px;text-align:center;font:400 14px var(--head)}
</style>
</head>
<body>
<div class="page">

  <header>
    <div class="abs topbar">
      <div class="info"><span>Call Us : +1 250 555 0147</span><span>|</span><span>Email : info@brevinelectric.ca</span></div>
    </div>
    <div class="abs brand-block"></div>
    <div class="abs brand"><div class="mark"></div><div class="name">BREVIN ELECTRIC Ltd</div></div>
    <nav class="abs nav"><span class="on">HOME</span><span>ABOUT US</span><span>SERVICES</span><span>BLOG</span><span>REVIEWS</span><span>CONTACT</span></nav>
    <div class="abs nav-search"></div>
  </header>

  <section class="abs hero">
    <div class="fill" style="inset:0" role="img" aria-label="Electrician testing a distribution panel with a multimeter"></div>
    <h1>Brevin<br>Electric Ltd</h1>
    <p>Sed ut perspiciatis unde omnis iste natus error sit voluptatem accusantium doloremque laudantium totam rem aperiam, eaque</p>
    <span class="btn">READ MORE</span>
    <div class="dots"><span></span><span class="on"></span><span></span></div>
  </section>

  <section class="services">
    <h2 class="abs title" style="top:880px">OUR <b>SERVICES</b></h2>
    <div class="abs rule" style="left:579px;top:932px"></div>
    <p class="abs sub" style="top:950px">Sed ut perspiciatis unde omnis iste natus error sit voluptatem accusantium doloremque</p>

    <article class="abs card" style="left:111px">
      <div class="photo" role="img" aria-label="Bright custom home kitchen" style="background:linear-gradient(135deg,#b89470,#e9e3d8 50%,#c9a57c)"></div>
      <h3>Custom Homes</h3>
      <p>Sed ut perspiciatis unde omnis iste natus error sit voluptatem accusantium dolorem que laudantium, totam rem</p>
      <div class="more">Read More</div>
    </article>
    <article class="abs card gold" style="left:446px">
      <div class="photo" role="img" aria-label="Gloved hands wiring a residential outlet" style="background:linear-gradient(135deg,#6f6b66,#2d3a66 50%,#c9a33a)"></div>
      <h3>Residential</h3>
      <p>Sed ut perspiciatis unde omnis iste natus error sit voluptatem accusantium dolorem que laudantium, totam rem</p>
      <div class="more">Read More</div>
    </article>
    <article class="abs card" style="left:780px">
      <div class="photo" role="img" aria-label="Electrician working on a commercial switchboard" style="background:linear-gradient(135deg,#5c6670,#8f9aa3 50%,#2d3d5c)"></div>
      <h3>Commercial</h3>
      <p>Sed ut perspiciatis unde omnis iste natus error sit voluptatem accusantium dolorem que laudantium, totam rem</p>
      <div class="more">Read More</div>
    </article>
  </section>

  <section class="about">
    <div class="abs frame"></div>
    <div class="abs pattern-area" role="img" aria-label="Decorative grid pattern"></div>
    <div class="abs about-photo" role="img" aria-label="Open commercial interior with exposed ceiling ducts"></div>
    <div class="abs badge"><div class="num">25</div><div class="lbl">YEARS' EXPERIENCE</div></div>
    <div class="abs about-text">
      <div class="hi">Welcome</div>
      <h2>Brevin Electric Ltd</h2>
      <div class="line"></div>
      <p>Sed ut perspiciatis unde omnis iste natus error sit voluptatem accusantium doloremque laudantium, totam rem aperiam, eaque ipsa quae ab illo inventore veritatis et quasi architecto beatae vitae dicta sunt explicabo. Nemo enim ipsam voluptatem quia voluptas sit aspernatur aut odit aut fugit, sed quia consequuntur magni dolores eos qui ratione voluptatem sequi nesciunt. Neque porro quisquam est, qui dolorem ipsum quia dolor sit amet, consectetur, adipisci velit, sed quia non numquam eius modi tempora incidunt ut labore et dolore magnam aliquam quaerat voluptatem.</p>
      <span class="btn">READ MORE</span>
    </div>
  </section>

  <section class="abs featured">
    <div class="fill" style="inset:0" role="img" aria-label="Electrician with tool belt carrying coiled cable"></div>
    <h2>FEATURED WORKS</h2>
    <div class="rule"></div>
    <p>Sed ut perspiciatis unde omnis iste natus error sit voluptatem accusantium doloremque laudantium, totam rem aperiam, eaque ipsa quae ab illo inventore veritatis et quasi architecto beatae vitae dicta sunt explicabo. Nemo enim ipsam volu ptatem quia voluptas sit aspernatur aut odit aut fugit, sed quia consequuntur magni dolores eos qui ratione voluptatem unde omnis iste natus sequi nesciunt.</p>
    <span class="btn">READ MORE</span>
  </section>

  <section class="blog">
    <h2 class="abs title" style="top:2882px">LATEST <b>BLOG</b></h2>
    <div class="abs rule" style="left:579px;top:2934px"></div>
    <p class="abs sub" style="top:2952px">Sed ut perspiciatis unde omnis iste natus error sit voluptatem accusantium doloremque</p>

    <article class="abs post" style="left:111px">
      <div class="photo" role="img" aria-label="Screwdriver adjusting circuit breakers" style="background:linear-gradient(135deg,#8c8a86,#c9c6c0 50%,#b54a3a)">
        <div class="date">06<small>AUG</small></div>
      </div>
      <h3>Sed ut perspiciatis unde omnis iste</h3>
      <p>Nemo enim ipsam voluptatem quia voluptas sit aspernatur aut odit aut fugit, sed quia consequuntur magni dolores eos qui ratione vol uptatem sequi nesciun</p>
    </article>
    <article class="abs post" style="left:611px">
      <div class="photo" role="img" aria-label="Industrial hall with hanging pendant lights" style="background:linear-gradient(135deg,#4f5a66,#a9b3bb 50%,#59636c)">
        <div class="date">06<small>AUG</small></div>
      </div>
      <h3>Sed ut perspiciatis unde omnis iste</h3>
      <p>Nemo enim ipsam voluptatem quia voluptas sit aspernatur aut odit aut fugit, sed quia consequuntur magni dolores eos qui ratione vol uptatem sequi nesciun</p>
    </article>
  </section>

  <section class="abs contact">
    <div class="cbrand" style="top:28px"><div class="mark"></div><div class="name">BREVIN ELECTRIC Ltd</div></div>
    <div class="crow" style="top:214px">
      <div class="ic"><svg width="16" height="20" viewBox="0 0 16 20"><path d="M8 1a6 6 0 0 0-6 6c0 5 6 12 6 12s6-7 6-12a6 6 0 0 0-6-6z" fill="none" stroke="#fff" stroke-width="2"/><circle cx="8" cy="7" r="2" fill="#fff"/></svg></div>
      <div><b>ADDRESS</b><span># Lorem Ipsum Dummy Lorem text</span></div>
    </div>
    <div class="crow" style="top:280px">
      <div class="ic"><svg width="18" height="18" viewBox="0 0 18 18"><path d="M4 1l3 4-2 2a11 11 0 0 0 6 6l2-2 4 3-2 3C8 17 1 10 1 3z" fill="#fff"/></svg></div>
      <div><b>PHONE</b><span>+1 250 555 0147</span></div>
    </div>
    <div class="crow" style="top:346px">
      <div class="ic"><svg width="18" height="14" viewBox="0 0 18 14"><rect x="1" y="1" width="16" height="12" fill="none" stroke="#fff" stroke-width="2"/><path d="M1 1l8 7 8-7" fill="none" stroke="#fff" stroke-width="2"/></svg></div>
      <div><b>EMAIL</b><span>info@brevinelectric.ca</span></div>
    </div>

    <h2>CONTACT US</h2>
    <div class="rule"></div>
    <div class="field" style="left:557px;top:122px;width:256px;height:44px">FIRST NAME :</div>
    <div class="field" style="left:832px;top:122px;width:256px;height:44px">LAST NAME :</div>
    <div class="field" style="left:557px;top:180px;width:256px;height:44px">EMAIL :</div>
    <div class="field" style="left:832px;top:180px;width:256px;height:44px">PHONE :</div>
    <div class="field" style="left:557px;top:236px;width:532px;height:130px">MESSAGE :</div>
    <div class="submit">SUBMIT</div>
  </section>

  <footer class="abs footer">
    <nav class="fnav"><span>HOME</span><span>ABOUT US</span><span>SERVICES</span><span>BLOG</span><span>REVIEWS</span><span>CONTACT</span></nav>
    <div class="fsoc">
      <span><svg width="14" height="14" viewBox="0 0 18 18"><path d="M4 1l3 4-2 2a11 11 0 0 0 6 6l2-2 4 3-2 3C8 17 1 10 1 3z" fill="#fff"/></svg></span>
      <span><svg width="16" height="12" viewBox="0 0 18 14"><rect x="1" y="1" width="16" height="12" fill="none" stroke="#fff" stroke-width="2"/><path d="M1 1l8 7 8-7" fill="none" stroke="#fff" stroke-width="2"/></svg></span>
      <span><svg width="12" height="16" viewBox="0 0 16 20"><path d="M8 1a6 6 0 0 0-6 6c0 5 6 12 6 12s6-7 6-12a6 6 0 0 0-6-6z" fill="none" stroke="#fff" stroke-width="2"/><circle cx="8" cy="7" r="2" fill="#fff"/></svg></span>
      <span><svg width="14" height="14" viewBox="0 0 14 14"><path d="M2 7h10M8 3l4 4-4 4" fill="none" stroke="#fff" stroke-width="2"/></svg></span>
      <span><svg width="14" height="14" viewBox="0 0 14 14"><path d="M2 7l3 3 7-7" fill="none" stroke="#fff" stroke-width="2"/></svg></span>
    </div>
    <p class="copy">© Copyright 2022 Brevin Electric Ltd.All Rights Reserved</p>
  </footer>

</div>
</body>
</html>
```